Vibrant business card design for Product person in Tech

I'm a 29 y/o female Product manager and I'd like to get a business card designed I can use when networking. I'd love something that stands out. Feel free to experiment with the use of colour, maybe geometrical elements - get creative! I work in the tech industry, so looking for a design without too much of a corporate feel. <br/><br/>The business card should have room for:<br/>Name<br/>Email address<br/>ProfileNet

Target Market(s)

Tech

Contact Information for Business Card

Name
Email
ProfileNet

Colors
faa54b
00a990
33b8a4
abd037
fbee3f
e667a6
ffcf3e
f59195

```html
<!DOCTYPE html>
<html lang="en">
<head>
<meta charset="utf-8">
<title>Business Card – Front and Back</title>
<link rel="stylesheet" href="https://fonts.googleapis.com/css2?family=Arimo:wght@700&display=swap">
<style>
  :root {
    --stage: #000000;
    --paper: #ffffff;
    --pink: #e667a6;
    --teal: #00a990;
    --teal-light: #33b8a4;
    --orange: #faa54b;
    --lime: #abd037;
    --ink: #000000;
  }
  html, body {
    margin: 0;
    padding: 0;
    width: 1200px;
    height: 1200px;
    overflow: hidden;
    background: var(--stage);
  }
  .canvas {
    display: block;
    width: 1200px;
    height: 1200px;
  }
  .card-text {
    font-family: "Arimo", Arial, sans-serif;
    font-weight: 700;
    fill: var(--ink);
  }
  .name { font-size: 48px; }
  .email { font-size: 28px; }
  .profile { font-size: 32px; }
</style>
</head>
<body>
<svg class="canvas" viewBox="0 0 1932 1932" xmlns="http://www.w3.org/2000/svg">
  <rect class="stage" width="1932" height="1932" fill="var(--stage)"/>

  <g class="card-front">
    <rect class="pattern-field" x="315" y="180" width="1342" height="766" fill="var(--pink)"
          role="img" aria-label="Pink background with a grid of outlined rounded squares"/>

    <g class="burst-left">
      <polygon points="315,180 1657,593 315,946" fill="var(--teal)"/>
      <polygon points="466,371 1657,593 315,946" fill="var(--orange)"/>
      <polygon points="560,490 1657,593 315,946" fill="var(--lime)"/>
    </g>

    <g class="burst-right">
      <polygon points="315,946 1657,593 1657,946" fill="var(--paper)"/>
      <polygon points="1330,946 1657,593 1467,946" fill="var(--lime)"/>
      <polygon points="1467,946 1657,593 1565,946" fill="var(--teal-light)"/>
      <polygon points="1565,946 1657,593 1657,946" fill="var(--orange)"/>
    </g>

    <polygon class="info-panel" points="1125,214 1616,214 1616,547 1125,398" fill="var(--paper)"/>

    <text class="card-text name" x="1362" y="288" text-anchor="middle">YOUR NAME</text>
    <text class="card-text email" x="1366" y="360" text-anchor="middle">your.email@company.com</text>
    <text class="card-text profile" x="1553" y="437" text-anchor="end">ProfileNet</text>
  </g>

  <rect class="card-back" x="315" y="995" width="1342" height="767" fill="var(--paper)"/>
</svg>
</body>
</html>
```